Health Care Company with Logo Needs Business Cards designed

We are a luxury behavioral health company looking for business cards design we already have a logo and are looking for someone to design a sophisticated luxurious looking business card. Please note that Card design should be captivating just like the logo and also encompass the logo color

Industry/Entity Type

Healthcare

Contact Information for Business Card

Logo,company name, tagline, my name and title, contact details, and physical address

```html
<!DOCTYPE html>
<html lang="en">
<head>
<meta charset="UTF-8">
<title>Orrin Behavioral Health – Business Cards</title>
<link href="https://fonts.googleapis.com/css2?family=Roboto:wght@400;500;900&family=Roboto+Condensed:wght@700&display=swap" rel="stylesheet">
<style>
  :root {
    --backdrop: #b9b9bb;
    --purple: #7d3f98;
    --sky: #14a0e4;
    --ink: #1d1d1f;
    --paper: #ffffff;
    --mist: #ededed;
  }
  * { margin: 0; padding: 0; box-sizing: border-box; }
  html, body { width: 1200px; height: 900px; overflow: hidden; }
  body {
    background: var(--backdrop);
    font-family: "Roboto", Arial, sans-serif;
    display: flex;
    align-items: center;
    justify-content: center;
    gap: 40px;
  }
  .card {
    position: relative;
    width: 540px;
    height: 309px;
    border-radius: 26px;
    overflow: hidden;
  }

  /* Front */
  .card-front {
    background: linear-gradient(200deg, var(--sky) 0%, #4a6cc0 28%, var(--purple) 62%, var(--purple) 100%);
    color: var(--paper);
  }
  .card-front .brand {
    position: absolute;
    left: 62px;
    top: 132px;
    display: flex;
    align-items: center;
    gap: 14px;
  }
  .brand-square {
    width: 36px;
    height: 36px;
    background: currentColor;
    flex-shrink: 0;
  }
  .brand-name {
    font-weight: 900;
    font-size: 30px;
    line-height: 1;
    white-space: nowrap;
  }
  .brand-tagline {
    font-weight: 500;
    font-size: 8.4px;
    letter-spacing: 2.5px;
    text-transform: uppercase;
    margin-top: 5px;
    white-space: nowrap;
  }

  /* Back */
  .card-back {
    background: var(--paper);
    color: var(--ink);
  }
  .card-back .side-band {
    position: absolute;
    right: 0;
    top: 0;
    width: 178px;
    height: 100%;
    background: var(--mist);
    clip-path: polygon(30% 0, 100% 0, 100% 100%, 0 100%);
  }
  .card-back .brand {
    position: absolute;
    left: 38px;
    top: 54px;
    display: flex;
    align-items: center;
    gap: 12px;
    color: var(--purple);
  }
  .card-back .brand-square { width: 30px; height: 30px; }
  .card-back .brand-name { font-size: 26px; }
  .card-back .brand-tagline { color: var(--sky); font-size: 7.2px; letter-spacing: 2.2px; }

  .person {
    position: absolute;
    left: 40px;
    top: 148px;
  }
  .person-name {
    font-family: "Roboto Condensed", Arial, sans-serif;
    font-weight: 700;
    font-size: 30px;
    color: var(--purple);
    line-height: 1;
  }
  .person-title {
    font-size: 15px;
    margin-top: 3px;
  }
  .contacts {
    list-style: none;
    margin-top: 12px;
    font-size: 14.5px;
    line-height: 1.45;
  }
  .contacts li { display: flex; align-items: center; gap: 8px; }
  .contacts svg { width: 14px; height: 14px; fill: none; stroke: var(--purple); stroke-width: 2; }
  .contacts .accent { color: var(--purple); }

  .address {
    position: absolute;
    right: 26px;
    top: 186px;
    text-align right;
    text-align: right;
    font-size: 14px;
    line-height: 1.3;
    font-style: normal;
  }
</style>
</head>
<body>

  <section class="card card-front" aria-label="Business card front">
    <div class="brand">
      <span class="brand-square"></span>
      <div>
        <div class="brand-name">Orrin Behavioral Health</div>
        <div class="brand-tagline">Steady care for calm and lasting renewal</div>
      </div>
    </div>
  </section>

  <section class="card card-back" aria-label="Business card back">
    <div class="side-band"></div>

    <div class="brand">
      <span class="brand-square"></span>
      <div>
        <div class="brand-name">Orrin Behavioral Health</div>
        <div class="brand-tagline">Steady care for calm and lasting renewal</div>
      </div>
    </div>

    <div class="person">
      <div class="person-name">Daniel Hart</div>
      <div class="person-title">Managing Director</div>
      <ul class="contacts">
        <li>
          <svg viewBox="0 0 24 24"><path d="M5 3h4l2 5-2.5 1.5a11 11 0 0 0 6 6L16 13l5 2v4a2 2 0 0 1-2 2A17 17 0 0 1 3 5a2 2 0 0 1 2-2z"/></svg>
          055-210 348 667
        </li>
        <li>
          <svg viewBox="0 0 24 24"><rect x="2" y="5" width="20" height="14" rx="1"/><path d="M2 6l10 7 10-7"/></svg>
          hello@orrinhealth.com
        </li>
        <li>
          <svg viewBox="0 0 24 24"><circle cx="12" cy="12" r="10"/><path d="M2 12h20M12 2c3 3 3 17 0 20M12 2c-3 3-3 17 0 20"/></svg>
          <span>www.<span class="accent">orrinhealth</span>.com</span>
        </li>
      </ul>
    </div>

    <address class="address">
      88 Linden Row, Suite 4<br>
      30518, Country Name
    </address>
  </section>

</body>
</html>
```